Book Cover Design Project

book cover: The Velvet Pardoner by Marjorie Talbrook

Here's a synopsis of the book: Noreen married rich and spent her days disapproving of her stepdaughter, shopping or seeing to it waiters and certain shop girls were fired. It all changed however after she was paid a visit in her palatial home. In her misadventures she makes some acquaintances and foes, but she is always stuck in the same situation. The bridges she has burned and the wrongs she has done have pushed their way into her life. Is she resigned to live the rest of her days like this? Will she roll up her sleeves and do something?

Sample chapter #1: http://pellowmark.examplepress.net/2013/02/08/chapter-1/

This will be an ebook so the illustration should look good as a thumbnail. Here are some covers that will show my tastes:
http://blog.glossvantry.co.uk/wp-content/uploads/2010/11/bannerblogblog.png

http://lacepage-reads.com/wp-content/uploads/2011/12/marian.jpg

http://www.fernwoodquilllists.com/TR/vlarge/9780061720147_0_Cover.jpg

http://2.img.postvellum.com/_UVDilWxjceA/SmEY9Ru9k5I/AAAAAAAAAJQ/6bFw3e_my-g/s400/corinna+hale+quiet+orchard+light.jpg
Updates

The Velvet Pardoner is a novella. If you have time, read the first chapter I put in my brief.

Industry/Entity Type

Shopping

Requirements
Must have
• The cover is TIFF (.tif/.tiff) or JPEG (.jpeg/.jpg) format
At least 1000 pixels on the longest side, with an ideal height/width ratio of 1.6.
2500 pixels on the longest side is preferred.
Nice to have
Should not have
• This story is a novella, it is not a novel. So it should not say novel.

```html
<!DOCTYPE html>
<html lang="en">
<head>
<meta charset="utf-8">
<title>The Velvet Pardoner — Marjorie Talbrook</title>
<link rel="stylesheet" href="https://fonts.googleapis.com/css2?family=Dosis:wght@600;700&family=Sniglet&display=swap">
<style>
  :root {
    --page: #ffffff;
    --teal: #6fcfcb;
    --pink: #e8336f;
    --violet: #6e2a8a;
    --lilac: #c9a9c9;
    --cream: #f3e6c6;
    --ink: #1e1418;
    --white: #ffffff;
  }
  * { margin: 0; padding: 0; box-sizing: border-box; }
  html, body {
    width: 1200px;
    height: 1000px;
    overflow: hidden;
    background: var(--page);
  }
  .canvas {
    position: relative;
    width: 1200px;
    height: 1000px;
  }
  .cover {
    position: absolute;
    left: 287px;
    top: 0;
    width: 625px;
    height: 1000px;
    background: var(--teal);
    overflow: hidden;
  }
  .cover-art {
    position: absolute;
    left: 0;
    top: 0;
    width: 625px;
    height: 1000px;
  }
  .author {
    position: absolute;
    top: 72px;
    right: 38px;
    width: 190px;
    text-align: center;
    font-family: "Sniglet", "Comic Sans MS", sans-serif;
    font-size: 36px;
    line-height: 44px;
    color: var(--white);
  }
  .author .by {
    display: block;
    font-size: 30px;
    margin-bottom: 4px;
  }
  .title {
    position: absolute;
    left: 0;
    right: 0;
    top: 562px;
    font-family: "Dosis", "Arial Narrow", sans-serif;
    font-weight: 700;
    color: var(--white);
    line-height: 1;
  }
  .title-lead {
    display: block;
    text-align: right;
    padding-right: 130px;
    font-size: 80px;
    letter-spacing: -1px;
  }
  .title-main {
    display: block;
    text-align: center;
    font-weight: 600;
    font-size: 158px;
    letter-spacing: -3px;
    margin-top: -6px;
  }
</style>
</head>
<body>
  <main class="canvas">
    <section class="cover">
      <svg class="cover-art" viewBox="0 0 625 1000" role="img" aria-label="Illustration: a stylish woman with a pink bob and striped round sunglasses, wrapped in a purple and lilac striped scarf, holding a large pink patterned handbag, on a teal background scattered with faint hearts">
        <defs>
          <linearGradient id="figure-tones" x1="0" y1="0" x2="0" y2="1">
            <stop offset="0" stop-color="#241a1e"/>
            <stop offset="0.12" stop-color="#e8336f"/>
            <stop offset="0.28" stop-color="#f3e6c6"/>
            <stop offset="0.42" stop-color="#b98fc0"/>
            <stop offset="0.58" stop-color="#6e2a8a"/>
            <stop offset="0.76" stop-color="#e8336f"/>
            <stop offset="1" stop-color="#3a1f2c"/>
          </linearGradient>
        </defs>
        <rect x="0" y="0" width="625" height="1000" fill="var(--teal)"/>
        <rect class="figure-upper" x="140" y="0" width="250" height="420" rx="40" fill="url(#figure-tones)"/>
        <rect class="figure-lower" x="0" y="380" width="580" height="620" rx="30" fill="url(#figure-tones)"/>
      </svg>

      <p class="author"><span class="by">by</span>Marjorie Talbrook</p>

      <h1 class="title">
        <span class="title-lead">The Velvet</span>
        <span class="title-main">Pardoner</span>
      </h1>
    </section>
  </main>
</body>
</html>
```